Dietitian needs a new business card design

I need a new business card design for my nutrition business that provides individual clinical nutrition advice for people with medical conditions. Business cards will be handed out to doctors, specialists and clients so will need to be sharp and project an image of professionalism

Target Market(s)

My clients are typically referred by doctors or specialists and the card will be used to handout to clients and their doctors.

Industry/Entity Type

Medical

Contact Information for Business Card

The business card will require the details below. These details can be found from my website https://www.kelvarrowclinic.com.au/

Font styles to use
Serif

Colors

Designer to choose colors to be used in the design.

Requirements
Must have
• 1. It needs be professional and contemporary
• 2. It needs to incorporate my logo
• 3. It needs space to write appointment times and dates
• 4. It needs to provide my phone number, fax number, email address and my web address
Nice to have
• Include the Registered Tovance Clinician Logo
• I have access to Framellow if required
• The locations I practise from
Should not have
• Pictures of food
• Spelling MIstakes

```html
<!DOCTYPE html>
<html lang="en">
<head>
<meta charset="utf-8">
<title>Tamberly Nutrition &amp; Dietetics – Business Card</title>
<link rel="stylesheet" href="https://fonts.googleapis.com/css2?family=Arimo:wght@400;700&display=swap">
<style>
  :root {
    --bg: #2a2a2a;
    --paper: #fbfbfb;
    --blue: #1c5aa6;
    --navy: #1e3f86;
    --green: #7cbb1f;
    --grey: #5d5d5d;
    --light-grey: #8a8a8a;
    --orange: #ef7a2b;
  }
  * { box-sizing: border-box; margin: 0; padding: 0; }
  html, body { width: 1200px; height: 997px; overflow: hidden; }
  body {
    background: var(--bg);
    font-family: "Arimo", Arial, sans-serif;
    position: relative;
  }
  .card {
    position: absolute;
    width: 560px;
    height: 320px;
    background: var(--paper);
    border-radius: 3px;
    overflow: hidden;
    box-shadow: 0 10px 30px rgba(0,0,0,.45);
  }
  .card--back { left: 25px; top: 330px; }
  .card--front { left: 615px; top: 330px; }
  .card__bands { position: absolute; inset: 0; }
  .card__url {
    position: absolute;
    right: 18px;
    bottom: 9px;
    color: #fff;
    font-size: 13px;
    font-weight: 700;
    letter-spacing: .2px;
  }

  /* back */
  .decor-circle {
    position: absolute;
    left: 230px; top: 30px;
    width: 210px; height: 210px;
    border-radius: 50%;
    background: radial-gradient(circle, rgba(124,187,31,.10), rgba(28,90,166,.06));
  }
  .locations { position: absolute; left: 28px; top: 28px; width: 260px; }
  .locations__title {
    font-size: 11px; font-weight: 700; color: var(--light-grey);
    letter-spacing: .6px; margin-bottom: 10px;
  }
  .location { display: flex; gap: 9px; margin-bottom: 9px; }
  .location__dot {
    flex: none; width: 10px; height: 10px; margin-top: 3px;
    border-radius: 50%; border: 3px solid var(--blue);
  }
  .location--green .location__dot { border-color: var(--green); }
  .location__name { font-size: 12.5px; font-weight: 700; color: var(--blue); }
  .location--green .location__name { color: var(--green); }
  .location__addr { font-size: 11.5px; color: var(--grey); line-height: 1.3; }
  .appointments { position: absolute; left: 300px; top: 34px; width: 230px; }
  .appointments__title {
    font-size: 11px; font-weight: 700; color: var(--blue); letter-spacing: .4px;
  }
  .appointments__line {
    height: 30px; border-bottom: 2px dotted var(--blue);
  }

  /* front */
  .badge {
    position: absolute; right: 22px; top: 18px;
    width: 58px; height: 28px; background: var(--orange); border-radius: 2px;
  }
  .badge::after {
    content: ""; position: absolute; right: 8px; top: 6px;
    width: 16px; height: 16px; background: #fff; border-radius: 2px;
  }
  .brand {
    position: absolute; left: 120px; top: 72px;
    display: flex; align-items: center; gap: 14px;
  }
  .brand__mark { width: 58px; height: 58px; border-radius: 50%; background: var(--green); }
  .brand__name {
    color: var(--navy); font-weight: 700; font-size: 34px; line-height: 1;
  }
  .brand__name small { display: block; font-size: 19px; margin-top: 4px; }
  .person { position: absolute; right: 28px; top: 168px; text-align: right; }
  .person__name { font-size: 17px; font-weight: 700; color: var(--navy); }
  .person__role { font-size: 15px; color: var(--green); }
  .contact-tab {
    position: absolute; left: 0; top: 184px;
    width: 30px; height: 90px; background: var(--blue);
    border-radius: 0 6px 6px 0;
    display: flex; flex-direction: column; justify-content: space-around; align-items: center;
    padding: 6px 0;
  }
  .contact-list { position: absolute; left: 46px; top: 190px; list-style: none; }
  .contact-list li { font-size: 15px; color: #222; line-height: 26px; }
</style>
</head>
<body>

<section class="card card--back" aria-label="Card back">
  <div class="decor-circle" role="img" aria-label="Faint brand emblem area"></div>
  <svg class="card__bands" viewBox="0 0 560 320" aria-hidden="true">
    <path d="M0 306 L300 276 L560 276 L560 320 L0 320 Z" fill="var(--green)"/>
    <path d="M300 320 L322 278 Q326 270 336 270 L560 270 L560 320 Z" fill="var(--blue)"/>
  </svg>
  <div class="locations">
    <p class="locations__title">THE LOCATIONS I PRACTISE FROM</p>
    <div class="location">
      <span class="location__dot"></span>
      <div><p class="location__name">ASHCOMBE DOCTORS SURGERY</p>
      <p class="location__addr">14 Wrenfield Road<br>Ashcombe 7260</p></div>
    </div>
    <div class="location location--green">
      <span class="location__dot"></span>
      <div><p class="location__name">BRINDLE MEDICAL</p>
      <p class="location__addr">3/118 Corran Road<br>Brindle 7250</p></div>
    </div>
    <div class="location">
      <span class="location__dot"></span>
      <div><p class="location__name">RIVERBEND HEALTH</p>
      <p class="location__addr">7 Harwick Drive<br>Riverbend 7250</p></div>
    </div>
    <div class="location location--green">
      <span class="location__dot"></span>
      <div><p class="location__name">ELMSTEAD MEDICAL CENTRE</p>
      <p class="location__addr">Cnr Lyle &amp; Garnet Streets<br>Elmstead 7250</p></div>
    </div>
  </div>
  <div class="appointments">
    <p class="appointments__title">APPOINTMENT TIMES AND DATES</p>
    <div class="appointments__line"></div>
    <div class="appointments__line"></div>
    <div class="appointments__line"></div>
    <div class="appointments__line"></div>
    <div class="appointments__line"></div>
  </div>
  <p class="card__url">www.kelvarrowclinic.com.au</p>
</section>

<section class="card card--front" aria-label="Card front">
  <div class="badge" role="img" aria-label="Registered Tovance Clinician badge"></div>
  <div class="brand">
    <span class="brand__mark"></span>
    <p class="brand__name">Tamberly<small>Nutrition &amp; Dietetics</small></p>
  </div>
  <div class="person">
    <p class="person__name">DEAN HALLOWAY</p>
    <p class="person__role">Director</p>
  </div>
  <svg class="card__bands" viewBox="0 0 560 320" aria-hidden="true">
    <path d="M0 306 L320 280 L560 280 L560 320 L0 320 Z" fill="var(--green)"/>
    <path d="M330 320 L350 280 Q354 272 364 272 L560 272 L560 320 Z" fill="var(--blue)"/>
  </svg>
  <div class="contact-tab" aria-hidden="true">
    <svg width="12" height="16" viewBox="0 0 12 16"><rect x="1" y="0.5" width="10" height="15" rx="2" fill="none" stroke="#fff" stroke-width="1.6"/><circle cx="6" cy="12.5" r="1" fill="#fff"/></svg>
    <svg width="15" height="11" viewBox="0 0 15 11"><rect x="0.5" y="0.5" width="14" height="10" fill="#fff"/><path d="M0.5 0.5 L7.5 6 L14.5 0.5" fill="none" stroke="var(--blue)" stroke-width="1.3"/></svg>
    <svg width="12" height="16" viewBox="0 0 12 16"><path d="M6 15 C2 10 0.5 7.5 0.5 5.5 A5.5 5.5 0 0 1 11.5 5.5 C11.5 7.5 10 10 6 15Z" fill="#fff"/><circle cx="6" cy="5.5" r="2" fill="var(--blue)"/></svg>
  </div>
  <ul class="contact-list">
    <li>555-014-2231</li>
    <li>555-018-7740</li>
    <li>dean@kelvarrowclinic.com.au</li>
  </ul>
  <p class="card__url">www.kelvarrowclinic.com.au</p>
</section>

</body>
</html>
```